BrovaLT BIZ Card, email signature & Stationary

Professional business cards, email signatures and ms word letterhead

Target Market(s)

business owners

Industry/Entity Type

cloud hosting

Contact Information for Business Card

name title office phone number , direct line, fax email address web site

Font styles to use
Other font styles liked:
• something that compliments font in logo

```html
<!DOCTYPE html>
<html lang="en">
<head>
<meta charset="utf-8">
<title>BrovaLT Business Card</title>
<link rel="stylesheet" href="https://fonts.googleapis.com/css2?family=Montserrat:wght@300;400;500;700&display=swap">
<style>
  :root {
    --backdrop: #5e534d;
    --card-dark: #1f1f21;
    --card-white: #ffffff;
    --panel-grey: #e1e1e1;
    --brand-red: #e31e24;
    --ink: #111111;
    --muted: #4a4a4a;
  }
  * { margin: 0; padding: 0; box-sizing: border-box; }
  html, body { width: 1200px; height: 1200px; overflow: hidden; }
  body {
    background: var(--backdrop);
    font-family: "Montserrat", sans-serif;
    position: relative;
  }
  .card { position: absolute; left: 179px; width: 861px; height: 494px; }
  .card-front { top: 85px; background: var(--card-dark); display: flex; align-items: center; justify-content: center; }
  .card-back { top: 622px; background: var(--card-white); }
  .brand-name {
    font-family: "Montserrat", sans-serif;
    font-weight: 300;
    color: var(--brand-red);
    line-height: 1;
    letter-spacing: 0.01em;
  }
  .card-front .brand-name { font-size: 74px; }
  .back-panel {
    position: absolute; left: 27px; top: 23px; right: 27px; bottom: 23px;
    background: var(--panel-grey);
  }
  .back-panel .brand-name { position: absolute; left: 30px; top: 36px; font-size: 66px; }
  .person { position: absolute; left: 30px; top: 345px; }
  .person-name { font-weight: 700; font-size: 31px; color: var(--ink); letter-spacing: 0.02em; line-height: 1.2; }
  .person-name .surname { color: var(--brand-red); }
  .person-title { font-weight: 400; font-size: 24px; color: var(--muted); letter-spacing: 0.12em; margin-top: 4px; }
  .contact { position: absolute; left: 445px; color: var(--muted); font-size: 25px; letter-spacing: 0.12em; }
  .address { top: 30px; line-height: 37px; }
  .phones { top: 189px; }
  .online { top: 345px; }
  .contact-row { display: flex; align-items: center; height: 37px; }
  .contact-row svg { width: 26px; height: 26px; fill: var(--brand-red); margin-right: 14px; flex: none; }
</style>
</head>
<body>
  <section class="card card-front">
    <span class="brand-name">BrovaLT</span>
  </section>

  <section class="card card-back">
    <div class="back-panel">
      <span class="brand-name">BrovaLT</span>

      <div class="person">
        <p class="person-name">NAME <span class="surname">SURENAME</span></p>
        <p class="person-title">DIRECTOR</p>
      </div>

      <address class="contact address" style="font-style:normal">
        48 Harbor Lane,<br>Suite 210, Aldenport<br>NV 89512
      </address>

      <div class="contact phones">
        <div class="contact-row">
          <svg viewBox="0 0 24 24" aria-hidden="true"><path d="M6.6 10.8a15 15 0 0 0 6.6 6.6l2.2-2.2a1 1 0 0 1 1-.25 11.4 11.4 0 0 0 3.6.6 1 1 0 0 1 1 1V20a1 1 0 0 1-1 1A17 17 0 0 1 3 4a1 1 0 0 1 1-1h3.5a1 1 0 0 1 1 1c0 1.25.2 2.45.6 3.6a1 1 0 0 1-.25 1z"/><path d="M14 3a7 7 0 0 1 7 7h-2a5 5 0 0 0-5-5zm0 4a3 3 0 0 1 3 3h-2a1 1 0 0 0-1-1z"/></svg>
          <span>444 555-0147</span>
        </div>
        <div class="contact-row">
          <svg viewBox="0 0 24 24" aria-hidden="true"><path d="M2 8c0-2 4-4 10-4s10 2 10 4v2h-5V8H7v2H2z"/><path d="M6 11h12l3 5v5H3v-5zm6 2a3 3 0 1 0 0 6 3 3 0 0 0 0-6z"/></svg>
          <span>888 555-0162</span>
        </div>
        <div class="contact-row">
          <svg viewBox="0 0 24 24" aria-hidden="true"><path d="M6 2h12v5H6z"/><path d="M3 8h18v9h-3v-3H6v3H3z"/><path d="M7 15h10v7H7z" fill="#fff"/><path d="M7 15h10v7H7zm1 1v5h8v-5z"/></svg>
          <span>888 555-0162</span>
        </div>
      </div>

      <div class="contact online">
        <div class="contact-row">
          <svg viewBox="0 0 24 24" aria-hidden="true"><path d="M2 5h20v14H2z"/><path d="M2 5l10 8 10-8" fill="none" stroke="#e1e1e1" stroke-width="1.6"/></svg>
          <span>info@brovalt.com</span>
        </div>
        <div class="contact-row">
          <svg viewBox="0 0 24 24" aria-hidden="true"><g fill="none" stroke="#e31e24" stroke-width="1.6"><circle cx="12" cy="12" r="10"/><ellipse cx="12" cy="12" rx="4.5" ry="10"/><path d="M2 12h20M4 7h16M4 17h16M12 2v20"/></g></svg>
          <span>www.brovalt.com</span>
        </div>
      </div>
    </div>
  </section>
</body>
</html>
```